Book Cover "Venice"

Creation of a cover (14 x 20.5 cm + bleed area) for a book:
Image: “BrumeVerte” (Tiff joined)
AUTHOR: Maribel Quonte
TITLE: The murmurs of Oldmere
PUBLISHER: Editions Plavoc (AT THE BOTTOM OF THE COVER)
Updates

Target Market(s)

Readers of romantic novels

Industry/Entity Type

Book

```html
<!DOCTYPE html>
<html lang="en">
<head>
<meta charset="utf-8">
<title>The Murmurs of Oldmere — Book Cover</title>
<link rel="stylesheet" href="https://fonts.googleapis.com/css2?family=Italiana&family=Poppins:wght@700&family=Oswald:wght@300&display=swap">
<style>
  :root {
    --stage: #b3b3b3;
    --sky-deep: #b8161c;
    --sky-red: #d92a1f;
    --sky-orange: #ea4a22;
    --sky-dusk: #8c1d24;
    --night: #060405;
    --title-dark: #120808;
    --title-light: #ffffff;
    --accent-yellow: #ffe000;
    --publisher: #ffffff;
  }
  * { margin: 0; padding: 0; box-sizing: border-box; }
  html, body {
    width: 1200px;
    height: 2400px;
    overflow: hidden;
    background: var(--stage);
  }
  .cover {
    position: absolute;
    left: 100px;
    top: 468px;
    width: 1000px;
    height: 1464px;
    background: var(--night);
    overflow: hidden;
    box-shadow: 0 18px 30px rgba(0, 0, 0, 0.35);
  }
  .cover-photo {
    position: absolute;
    left: 0;
    top: 0;
    width: 1000px;
    height: 1180px;
    background:
      linear-gradient(180deg,
        var(--sky-deep) 0%,
        var(--sky-red) 20%,
        var(--sky-orange) 42%,
        var(--sky-red) 60%,
        var(--sky-dusk) 74%,
        #2a0b0d 86%,
        var(--night) 100%);
  }
  .title {
    position: absolute;
    left: 0;
    top: 70px;
    width: 100%;
    text-align: center;
    font-family: "Italiana", "Bodoni Moda", serif;
    font-weight: 400;
    line-height: 1;
    text-transform: uppercase;
  }
  .title span { display: block; }
  .title-the {
    color: var(--title-dark);
    font-size: 132px;
    letter-spacing: -4px;
  }
  .title-murmurs {
    color: var(--title-light);
    font-size: 124px;
    letter-spacing: -5px;
    margin-top: -6px;
  }
  .title-of {
    color: var(--title-light);
    font-size: 124px;
    letter-spacing: -4px;
    margin-top: -6px;
  }
  .title-place {
    color: var(--accent-yellow);
    font-size: 196px;
    letter-spacing: -10px;
    margin-top: -10px;
  }
  .author {
    position: absolute;
    left: 0;
    top: 1210px;
    width: 100%;
    text-align: center;
    font-family: "Poppins", "Montserrat", sans-serif;
    font-weight: 700;
    font-size: 46px;
    letter-spacing: 11px;
    color: var(--accent-yellow);
    text-transform: uppercase;
  }
  .publisher {
    position: absolute;
    left: 0;
    top: 1318px;
    width: 100%;
    text-align: center;
    font-family: "Oswald", "Roboto Condensed", sans-serif;
    font-weight: 300;
    font-size: 28px;
    letter-spacing: 6px;
    color: var(--publisher);
    text-transform: uppercase;
  }
</style>
</head>
<body>
  <main class="cover">
    <div class="cover-photo" role="img" aria-label="Photograph of a blazing red sunset sky over a silhouetted domed church skyline with glowing street lanterns"></div>
    <h1 class="title">
      <span class="title-the">The</span>
      <span class="title-murmurs">Murmurs</span>
      <span class="title-of">of</span>
      <span class="title-place">Oldmere</span>
    </h1>
    <p class="author">Maribel Quonte</p>
    <p class="publisher">Editions Plavoc</p>
  </main>
</body>
</html>
```